New Signage Design Project

Hi Corwin, you undertook some design work for our business (business card design) about 12 months ago and we would now like to develop signage for our business using this design. The signage design we are looking for is square in shape and will cover a large area approximately 1.6m x 1.6m.

I'm hoping this will be quite straight forward. We are looking to fill out/extent the background (vertically and out) so that it will suit a square sign.

```html
<!DOCTYPE html>
<html lang="en">
<head>
<meta charset="utf-8">
<title>Norvale Trading – Square Sign 1.6 m</title>
<link rel="stylesheet" href="https://fonts.googleapis.com/css2?family=Montserrat:wght@500&family=Mulish:wght@400&display=swap">
<style>
  :root {
    --board: #000000;
    --sign: #ffffff;
    --navy: #2d4d68;
    --mist-green: #e2f4e6;
    --mist-blue: #dbeaf5;
    --caption: #ffffff;
  }
  html, body {
    margin: 0;
    padding: 0;
    width: 1200px;
    height: 1200px;
    overflow: hidden;
    background: var(--board);
  }
  .board {
    position: relative;
    width: 1200px;
    height: 1200px;
    background: var(--board);
  }
  .sign {
    position: absolute;
    left: 62px;
    top: 24px;
    width: 1084px;
    height: 1083px;
    background: var(--sign);
    overflow: hidden;
  }
  .sign-backdrop {
    position: absolute;
    inset: 12px;
    background:
      radial-gradient(circle at 50% 50%, var(--sign) 0%, var(--sign) 38%, rgba(255,255,255,0) 62%),
      linear-gradient(135deg, var(--mist-green) 0%, var(--mist-blue) 45%, var(--mist-blue) 55%, var(--mist-green) 100%);
  }
  .brand {
    position: absolute;
    left: 0;
    right: 0;
    top: 470px;
    text-align: center;
    color: var(--navy);
    font-family: "Montserrat", sans-serif;
    font-weight: 500;
  }
  .brand-name {
    margin: 0;
    font-size: 108px;
    line-height: 1;
    letter-spacing: 0.2em;
    margin-right: -0.2em;
  }
  .brand-tagline {
    margin: 14px 0 0;
    font-size: 46px;
    line-height: 1;
    letter-spacing: 0.62em;
    margin-right: -0.62em;
  }
  .size-caption {
    position: absolute;
    left: 0;
    right: 0;
    top: 1140px;
    text-align: center;
    color: var(--caption);
    font-family: "Mulish", sans-serif;
    font-weight: 400;
    font-size: 27px;
    letter-spacing: 0.02em;
  }
</style>
</head>
<body>
  <main class="board">
    <section class="sign">
      <div class="sign-backdrop" role="img" aria-label="Soft pale green and blue splash pattern framing the centre of the sign"></div>
      <div class="brand">
        <h1 class="brand-name">NORVALE</h1>
        <p class="brand-tagline">TRADING</p>
      </div>
    </section>
    <p class="size-caption">SIZE 1.6 mtr X 1.6 tmr</p>
  </main>
</body>
</html>
```